Label for packages of Pure Raw Natural Honeycomb

This is a label that will be used to sell pure raw honeycomb on the internet and in farm gate sales
Label must contain my Logo (which is attached)
my website www.hivelanterngold.ca
the weight 300 gr and the words Pure Raw Honeycomb
label design should fit onto a sticker 3" by 2" oval but If the size appears to small to get all that info on I am willing to look at a different size or shape

Target Market(s)

internet and in person farm gate customers

Industry/Entity Type

Agriculture

Font styles to use
Other font styles liked:
• the font should compliment my logo font

Colors
ffc214

Requirements
Must have
• Label must contain my Logo (attached) my website www.hivelanterngold.ca
• the weight 300 gr and the words Pure Raw Honeycomb would like something in black and gold with a bit of an Elegant vintage feel
Nice to have
• vintage feel
• If the size appears to small to get all that info on I am willing to look at a different size or shape
Should not have
• no cartoons

```html
<!DOCTYPE html>
<html lang="en">
<head>
<meta charset="utf-8">
<title>Hive Lantern Gold – Pure Raw Honeycomb Label</title>
<link rel="stylesheet" href="https://fonts.googleapis.com/css2?family=Uncial+Antiqua&family=Arimo:wght@700&display=swap">
<style>
  :root {
    --label-black: #0b0a08;
    --label-gold: #d8b468;
    --ribbon-gold-light: #fbe27a;
    --ribbon-gold: #f2c80a;
    --ribbon-gold-dark: #b88a0c;
    --paper: #ffffff;
  }
  html, body {
    margin: 0;
    padding: 0;
    width: 1200px;
    height: 1199px;
    overflow: hidden;
    background: var(--paper);
  }
  .label-canvas {
    display: block;
    width: 1200px;
    height: 1199px;
  }
  .brand-name {
    font-family: "Uncial Antiqua", serif;
    font-size: 36px;
    fill: var(--label-gold);
  }
  .product-title {
    font-family: "Uncial Antiqua", serif;
    font-size: 46px;
    fill: var(--label-black);
  }
  .net-weight {
    font-family: "Arimo", Arial, sans-serif;
    font-weight: 700;
    font-size: 33px;
    fill: var(--label-gold);
  }
</style>
</head>
<body>
<svg class="label-canvas" viewBox="0 0 1200 1199" xmlns="http://www.w3.org/2000/svg">
  <defs>
    <linearGradient id="ribbonFill" x1="0" y1="0" x2="0" y2="1">
      <stop offset="0" stop-color="var(--ribbon-gold-light)"/>
      <stop offset="0.5" stop-color="var(--ribbon-gold)"/>
      <stop offset="1" stop-color="var(--ribbon-gold-dark)"/>
    </linearGradient>
    <radialGradient id="flourishTone">
      <stop offset="0" stop-color="var(--label-gold)" stop-opacity="0.55"/>
      <stop offset="1" stop-color="var(--label-gold)" stop-opacity="0"/>
    </radialGradient>
  </defs>

  <!-- hexagon label body -->
  <polygon class="hex-outer" points="611,172 959,377 959,788 611,993 265,788 265,377" fill="var(--label-black)"/>
  <polygon class="hex-rule-thin" points="611,190 943,386 943,779 611,975 281,779 281,386"
           fill="none" stroke="var(--label-gold)" stroke-width="3"/>
  <polygon class="hex-rule-thick" points="611,202 932,392 932,773 611,963 292,773 292,392"
           fill="none" stroke="var(--label-gold)" stroke-width="5"/>

  <!-- honeycomb field -->
  <polygon class="honeycomb-field" role="img" aria-label="Gold honeycomb cell pattern on black"
           points="611,212 924,397 924,768 611,953 300,768 300,397" fill="#16130d"/>

  <!-- side flourishes -->
  <ellipse class="flourish-left" role="img" aria-label="Gold vintage scroll ornament" cx="365" cy="495" rx="92" ry="72" fill="url(#flourishTone)"/>
  <ellipse class="flourish-right" role="img" aria-label="Gold vintage scroll ornament" cx="857" cy="495" rx="92" ry="72" fill="url(#flourishTone)"/>
  <ellipse class="flourish-bottom" role="img" aria-label="Gold vintage scroll ornaments around weight" cx="611" cy="822" rx="170" ry="52" fill="url(#flourishTone)"/>

  <!-- brand medallion -->
  <circle class="brand-medallion" cx="611" cy="458" r="164" fill="var(--label-black)" stroke="var(--label-gold)" stroke-width="4"/>
  <circle class="brand-dot" cx="611" cy="398" r="14" fill="none" stroke="var(--label-gold)" stroke-width="4"/>
  <text class="brand-name" x="611" y="465" text-anchor="middle">Hive Lantern</text>
  <text class="brand-name" x="611" y="510" text-anchor="middle">Gold</text>

  <!-- product ribbon -->
  <path class="product-ribbon" d="M273,620 Q611,670 945,620 L937,702 Q611,758 281,702 Z"
        fill="url(#ribbonFill)" stroke="var(--ribbon-gold-dark)" stroke-width="1.5"/>
  <text class="product-title" x="611" y="697" text-anchor="middle">Pure Raw Honeycomb</text>

  <!-- net weight -->
  <ellipse class="weight-oval" cx="611" cy="823" rx="85" ry="37" fill="var(--label-black)" stroke="var(--label-gold)" stroke-width="3"/>
  <text class="net-weight" x="611" y="835" text-anchor="middle">300 gr</text>
</svg>
</body>
</html>
```